Spring Pet Banner for Veterinary Hospital 5m x 1.2m

Meadowbrook Pet Hospital is a Veterinary Hospital that treats Dogs and Cats. I want a new poster to go on our front fence for spring. It's 5m x 1.2m. I want a design that is eye catching from a nearby road that promotes preventative health measures to get ready for spring.
I have attached images that we commonly use in our branding. I would like images that suite the mood of these images.
EDIT: I have just uploaded a design that I knocked up. I think it sends a clear message.....but I am not a graphic designer or marketing expert, so you can make a similar design if you want and clean it up.
Updates

Need extra days to review

The plan I had for the design is not working. I have simplified the plan so designers can use their own ideas.

Target Market(s)

Women Aged 18 to 60.

Industry/Entity Type

Veterinary

Font styles to use
Sans Serif

Colors
9bcb3b
f78f20
f37122

Requirements
Must have
• Visible from road 30m away.
• Spring.
• A call to action.
• Compliment existing branding.
Nice to have
• Gives people a reason to bring their animals to us now.
Should not have
• Clip art.

```html
<!DOCTYPE html>
<html lang="en">
<head>
<meta charset="utf-8">
<title>Meadowbrook Pet Hospital – Spring Banner</title>
<link href="https://fonts.googleapis.com/css2?family=Montserrat:wght@600;700;800&family=Ubuntu:wght@500&display=swap" rel="stylesheet">
<style>
  :root {
    --backdrop: #d6d6d6;
    --cream: #fdfbe9;
    --green: #5a8424;
    --brown: #5b3b1a;
    --brown-dark: #3b2914;
    --white: #ffffff;
    --ink: #111111;
  }
  * { margin: 0; padding: 0; box-sizing: border-box; }
  html, body { width: 1200px; height: 1200px; overflow: hidden; }
  body { background: var(--backdrop); position: relative; font-family: "Montserrat", sans-serif; }

  .banner {
    position: absolute; left: 26px; top: 502px;
    width: 1148px; height: 274px;
    background: var(--cream);
    overflow: hidden;
    box-shadow: 0 6px 10px rgba(0,0,0,0.25);
  }
  .banner-shapes { position: absolute; inset: 0; width: 100%; height: 100%; }

  .headline {
    position: absolute; left: 300px; width: 776px; top: 48px;
    text-align: center; color: var(--ink);
    font-weight: 800; font-size: 55px; line-height: 1; letter-spacing: -0.5px;
  }
  .headline-pill {
    position: absolute; left: 478px; top: 102px; width: 422px; height: 38px;
    background: var(--brown); border-radius: 19px;
    color: var(--white); text-align: center;
    font-weight: 700; font-size: 29px; line-height: 38px;
  }
  .tagline {
    position: absolute; left: 438px; width: 500px; top: 149px;
    text-align: center; color: var(--brown-dark);
    font-weight: 600; font-size: 16px; line-height: 18px;
  }

  .brand-badge {
    position: absolute; left: 924px; top: 37px; width: 204px; height: 204px;
    border-radius: 50%; background: var(--white);
    border: 3px solid var(--brown);
    display: flex; flex-direction: column; align-items: center; justify-content: center;
  }
  .brand-name {
    font-family: "Ubuntu", sans-serif; font-weight: 500;
    color: var(--brown); font-size: 21px; line-height: 1.2; text-align: center;
  }
</style>
</head>
<body>
  <section class="banner">
    <svg class="banner-shapes" viewBox="0 0 1434 343" preserveAspectRatio="none">
      <defs>
        <linearGradient id="photo-tones" x1="0" y1="0" x2="0" y2="1">
          <stop offset="0" stop-color="#d9e6e0"/>
          <stop offset="0.45" stop-color="#c9b79a"/>
          <stop offset="1" stop-color="#8a6a3e"/>
        </linearGradient>
        <radialGradient id="badge-shadow" cx="0.5" cy="0.5" r="0.5">
          <stop offset="0" stop-color="#2f4a12" stop-opacity="0.6"/>
          <stop offset="1" stop-color="#2f4a12" stop-opacity="0"/>
        </radialGradient>
      </defs>
      <!-- ground wave -->
      <path d="M560 222 C690 290 850 300 1010 280 C1160 262 1300 240 1434 236" fill="none" stroke="#5b3b1a" stroke-width="7"/>
      <path d="M560 232 C690 298 850 308 1010 290 C1160 272 1300 252 1434 248" fill="none" stroke="#ffffff" stroke-width="6"/>
      <path d="M560 238 C690 304 850 314 1010 296 C1160 278 1300 258 1434 254 V343 H0 V238 Z" fill="#5a8424"/>
      <ellipse cx="1280" cy="310" rx="110" ry="12" fill="url(#badge-shadow)"/>
      <!-- side crescent -->
      <path d="M0 0 H505 C575 90 590 240 548 343 H0 Z" fill="#5a8424"/>
      <path d="M0 0 H492 C560 90 572 240 528 343 H0 Z" fill="#ffffff"/>
      <path d="M0 0 H486 C552 90 562 240 518 343 H0 Z" fill="#5b3b1a"/>
      <path d="M0 0 H481 C544 90 552 240 508 343 H0 Z" fill="#ffffff"/>
      <path d="M0 0 H478 C540 90 548 240 504 343 H0 Z" fill="url(#photo-tones)" role="img" aria-label="Photo: a woman lying in dry spring grass hugging and kissing her dog"/>
    </svg>

    <h1 class="headline">SPRING FOR A</h1>
    <div class="headline-pill">VETERINARY HOSPITAL</div>
    <p class="tagline">The most compelling reason to come<br>to us it to protect from Parvovirus.</p>

    <div class="brand-badge">
      <div class="brand-name">MEADOWBROOK<br>PET HOSPITAL</div>
    </div>
  </section>
</body>
</html>
```